Velvet Strut

The site will showcase the different drag queens of Manchester and provide an area for photography, video, social media feeds (such as zingo and Kinloop) as well as reviews of Drag queens to give the public a place to discuss shows or individuals.

Target Market(s)

Gay men

Industry/Entity Type

Media

Font styles to use
Decorative

Colors

Designer to choose colors to be used in the design.

Requirements
Must have
• Bright, bold, showbiz, glamorous but a little tacky at the same time.

```html
<!DOCTYPE html>
<html lang="en">
<head>
<meta charset="utf-8">
<title>Velvet Strut</title>
<link rel="stylesheet" href="https://fonts.googleapis.com/css2?family=Oswald:wght@300;400&family=Open+Sans:wght@400;700&display=swap">
<style>
:root{
  --black:#000;
  --slate:#3d3a3f;
  --slate-card:#2f2c31;
  --footer:#454348;
  --pink:#ff5fb4;
  --white:#fff;
  --muted:#c9c6cc;
  --text-dark:#d8d6da;
  --purple-a:#5b1a8a;
  --purple-b:#a13fc2;
  --purple-c:#d86fd6;
}
*{margin:0;padding:0;box-sizing:border-box}
html,body{width:1200px;height:2311px;overflow:hidden;background:var(--slate)}
body{position:relative;font-family:"Open Sans",Arial,sans-serif;color:var(--white)}
.abs{position:absolute}
.heading{font-family:"Oswald",Arial,sans-serif;font-weight:300;font-size:40px;line-height:1;text-transform:uppercase;color:var(--white)}
.read-more{font-size:15px;font-weight:700;color:var(--pink)}
.read-more::before{content:"";display:inline-block;border-left:6px solid var(--pink);border-top:5px solid transparent;border-bottom:5px solid transparent;margin-right:5px;vertical-align:1px}

.top-bar{left:0;top:0;width:1200px;height:37px;background:var(--black)}
.account-links{right:73px;top:9px;font-size:15px;font-weight:700;letter-spacing:.3px}
.masthead{left:0;top:37px;width:1200px;height:184px;
  background:radial-gradient(circle at 55% 30%,var(--purple-c) 0%,transparent 45%),
             linear-gradient(90deg,var(--purple-a),var(--purple-b) 50%,#7d2ba6 100%)}
.brand{left:67px;top:60px;font-family:"Oswald",Arial,sans-serif;font-weight:400;font-size:44px;letter-spacing:1px;text-transform:uppercase}
.social{position:absolute;top:48px;width:44px;height:44px;border-radius:50%;background:rgba(255,255,255,.35)}
.main-nav{left:0;top:221px;width:1200px;height:64px;background:var(--black)}
.main-nav ul{list-style:none}
.main-nav li{position:absolute;top:15px;font-family:"Oswald",Arial,sans-serif;font-size:26px;font-weight:300;text-transform:uppercase;white-space:nowrap;color:var(--white)}
.caret{display:inline-block;border-top:7px solid var(--white);border-left:6px solid transparent;border-right:6px solid transparent;margin-left:10px;vertical-align:5px}

.queens{left:0;top:285px;width:1200px;height:765px;background:var(--slate)}
.queen-card{position:absolute;top:125px;width:334px;height:480px;background:var(--black)}
.queen-photo{height:333px}
.queen-name{position:absolute;left:23px;top:352px;font-size:28px;font-weight:400;line-height:1}
.queen-blurb{position:absolute;left:23px;top:392px;width:290px;font-size:14px;line-height:18px}
.queen-card .read-more{position:absolute;left:23px;top:440px}
.intro{left:69px;top:651px;width:760px;font-size:15px;line-height:21px;color:var(--text-dark)}
.cta{left:890px;top:647px;width:241px;height:62px;background:var(--pink);font-family:"Oswald",Arial,sans-serif;font-size:25px;font-weight:300;text-transform:uppercase;display:flex;align-items:center;justify-content:center}

.news-band{left:0;top:1050px;width:1200px;height:658px;background:var(--black)}
.news-card{position:absolute;left:69px;width:515px;background:var(--slate)}
.news-title{font-family:"Oswald",Arial,sans-serif;font-weight:300;font-size:25px;text-transform:uppercase;line-height:1}
.news-date{font-size:15px;font-weight:700;margin-top:4px}
.news-text{font-size:15px;line-height:20px;color:var(--text-dark);margin-top:4px}
.comment{position:absolute;left:616px;width:515px;background:var(--slate);padding:18px 22px;font-size:14.5px;line-height:20px;color:var(--text-dark)}
.comment b{color:var(--white)}
.comment .ref{color:var(--pink)}

.feeds{left:0;top:1708px;width:1200px;height:451px;background:var(--slate)}
.thumb{position:absolute;width:90px;height:90px}
.tweet{position:absolute;left:435px;width:332px;height:91px;background:var(--slate-card);padding:14px 22px;font-size:14px;line-height:18px;color:#8f8c93}
.tweet .when{color:var(--white);margin-top:4px}
.kin-widget{left:801px;top:1816px;width:318px;height:283px;background:#101419;border:1px solid #222;overflow:hidden}
.kin-bar{font-size:11px;font-weight:700;padding:4px 6px;background:#1c2229}
.kin-row{display:flex;align-items:center;gap:8px;padding:8px 10px}
.kin-mark{width:52px;height:52px;background:#3b5171}
.kin-name{font-size:14px;font-weight:700}
.kin-like{display:inline-block;margin-top:4px;background:#4a63a0;font-size:11px;font-weight:700;padding:1px 6px}
.kin-count{font-size:11px;color:#99a;padding:0 10px 6px;border-bottom:1px solid #333;margin:0 6px}
.kin-faces{display:grid;grid-template-columns:repeat(6,44px);gap:5px;padding:8px 10px}
.kin-faces span{height:44px}
.kin-foot{font-size:11px;padding:6px 10px;border-top:1px solid #333;margin:0 6px}

.site-footer{left:0;top:2159px;width:1200px;height:152px;background:radial-gradient(circle at 30% 40%,#55525a,var(--footer) 60%);text-align:center;font-size:13px;line-height:21px;text-transform:uppercase;padding-top:44px;letter-spacing:.3px}
</style>
</head>
<body>

<div class="abs top-bar"></div>
<div class="abs account-links">LOGIN | REGISTER</div>

<header class="abs masthead">
  <div class="abs brand">Velvet Strut</div>
  <span class="social" style="left:928px"></span>
  <span class="social" style="left:980px"></span>
  <span class="social" style="left:1032px"></span>
  <span class="social" style="left:1085px"></span>
</header>

<nav class="abs main-nav">
  <ul>
    <li style="left:69px">Home</li>
    <li style="left:171px">What's On?<span class="caret"></span></li>
    <li style="left:356px">News &amp; Reviews<span class="caret"></span></li>
    <li style="left:583px">Media Gallery<span class="caret"></span></li>
    <li style="left:788px">About Us</li>
    <li style="left:926px">Contact Us</li>
  </ul>
</nav>

<section class="abs queens">
  <h2 class="abs heading" style="left:75px;top:56px">Drag Queens</h2>

  <article class="queen-card" style="left:69px">
    <div class="queen-photo" role="img" aria-label="Portrait of a drag queen with long red hair" style="background:radial-gradient(circle at 50% 45%,#c65a4a,#4a1410 75%)"></div>
    <h3 class="heading queen-name">Dixie Lamé</h3>
    <p class="queen-blurb">Lorem ipsum dolor sit amet, con-<br>sectetur</p>
    <a class="read-more">Read More</a>
  </article>

  <article class="queen-card" style="left:433px">
    <div class="queen-photo" role="img" aria-label="Portrait of a drag performer in purple drape" style="background:radial-gradient(circle at 50% 40%,#b07a68,#4a1658 70%)"></div>
    <h3 class="heading queen-name">Dixie Lamé</h3>
    <p class="queen-blurb">Lorem ipsum dolor sit amet, con-<br>sectetur</p>
    <a class="read-more">Read More</a>
  </article>

  <article class="queen-card" style="left:797px">
    <div class="queen-photo" role="img" aria-label="Drag performer on stage under spotlights" style="background:radial-gradient(circle at 30% 20%,#8aa0c8,#1b1e2c 70%)"></div>
    <h3 class="heading queen-name">Dixie Lamé</h3>
    <p class="queen-blurb">Lorem ipsum dolor sit amet, con-<br>sectetur</p>
    <a class="read-more">Read More</a>
  </article>

  <p class="abs intro">Lorem ipsum dolor sit amet, consectetur adipiscing elit. Nulla suscipit imperdiet quam sit amet ullamcorper. Interdum et malesuada fames ac ante ipsum primis in faucibus.<br><br>Quisque semper enim ut enim bibendum fermentum.</p>
  <a class="abs cta">Aliquam Commodo</a>
</section>

<section class="abs news-band">
  <h2 class="abs heading" style="left:69px;top:75px">Latest News</h2>
  <h2 class="abs heading" style="left:616px;top:75px">Latest Coments</h2>

  <article class="news-card" style="top:125px;height:243px;display:flex">
    <div role="img" aria-label="Close-up photo of red lips and cherries" style="width:226px;height:243px;flex:none;background:radial-gradient(circle at 55% 45%,#c04040,#3a0e12 75%)"></div>
    <div style="padding:22px 16px 0 21px;width:289px">
      <h3 class="news-title">Lorem Ipsum Dolor</h3>
      <p class="news-date">17 August 2014</p>
      <p class="news-text">Lorem ipsum dolor sit amet, consectetur adipiscing elit. Nulla suscipit imperdiet quam sit amet ullamcorper. Interdum et malesuada [...]</p>
      <p class="read-more" style="margin-top:16px">Read More</p>
    </div>
  </article>

  <article class="news-card" style="top:398px;height:193px;padding:24px 25px">
    <h3 class="news-title">Lorem Ipsum Dolor</h3>
    <p class="news-date">17 August 2014</p>
    <p class="news-text">Lorem ipsum dolor sit amet, consectetur adipiscing elit. Nulla suscipit imperdiet quam sit amet ullamcorper. Interdum et malesuada [...]</p>
    <p class="read-more" style="margin-top:8px">Read More</p>
  </article>

  <div class="comment" style="top:127px;height:102px"><b>Nola Sequin says:</b> Nam at ultricies massa. Aenean nunc purus, tempus eu pharetra vel, lobortis dignissim orci. Cras ac consequat nisl, in malesuada sem. <span class="ref">On: Curabitur ut ultricies tellus.</span></div>
  <div class="comment" style="top:260px;height:102px"><b>Dixie Lamé says:</b> Donec ac dolor viverra, condimentum sem eget, vulputate ante. Quisque rutrum, orci eu varius pharetra, quam justo consequat lorem. <span class="ref">On: Curabitur ut ultricies tellus.</span></div>
  <div class="comment" style="top:387px;height:102px"><b>Tansy Sequin says:</b> In pulvinar tincidunt egestas. Donec tempor sagittis nunc ac dictum. Sed molestie orci. <span class="ref">On: Curabitur ut ultricies tellus.</span></div>
</section>

<section class="abs feeds">
  <h2 class="abs heading" style="left:69px;top:62px">Snapframe</h2>
  <h2 class="abs heading" style="left:435px;top:62px">Zings</h2>
  <h2 class="abs heading" style="left:801px;top:62px">Kinloop</h2>

  <div class="thumb" role="img" aria-label="Performer on stage" style="left:69px;top:110px;background:linear-gradient(135deg,#2a3a6a,#7a4a6a)"></div>
  <div class="thumb" role="img" aria-label="Drag queen portrait" style="left:185px;top:110px;background:linear-gradient(135deg,#b89080,#6a4a50)"></div>
  <div class="thumb" role="img" aria-label="Venue interior" style="left:302px;top:110px;background:linear-gradient(135deg,#5a3a30,#a05a40)"></div>
  <div class="thumb" role="img" aria-label="Close-up of red lips" style="left:69px;top:232px;background:linear-gradient(135deg,#d08a88,#8a2a30)"></div>
  <div class="thumb" role="img" aria-label="Drag performer in purple" style="left:185px;top:232px;background:linear-gradient(135deg,#a07060,#5a2060)"></div>
  <div class="thumb" role="img" aria-label="City street at night" style="left:302px;top:232px;background:linear-gradient(135deg,#3a3a48,#8a7a70)"></div>
  <a class="abs read-more" style="left:69px;top:347px">Follow us on Snapframe</a>

  <div class="tweet" style="top:110px">Morbi tempor tincidunt turpis, eget frin-<br>gilla augue molestie vel.<p class="when">@ 17 August 2014</p></div>
  <div class="tweet" style="top:229px">Morbi tempor tincidunt turpis, eget frin-<br>gilla augue molestie vel.<p class="when">@ 17 August 2014</p></div>
  <a class="abs read-more" style="left:435px;top:347px">Follow us on zingo</a>
</section>

<div class="abs kin-widget">
  <div class="kin-bar">Find us on Kinloop</div>
  <div class="kin-row">
    <span class="kin-mark"></span>
    <div><div class="kin-name">Kinloop Makers</div><span class="kin-like">Like</span></div>
  </div>
  <div class="kin-count">3,157,444 people like Kinloop Makers.</div>
  <div class="kin-faces" role="img" aria-label="Grid of follower profile pictures">
    <span style="background:#4a3a3a"></span><span style="background:#7a5a6a"></span><span style="background:#8a7a6a"></span><span style="background:#6a8a4a"></span><span style="background:#5a6a8a"></span><span style="background:#8a6a5a"></span>
    <span style="background:#6a4a3a"></span><span style="background:#9a8a8a"></span><span style="background:#b0a8a0"></span><span style="background:#8a7a9a"></span><span style="background:#3a6a7a"></span><span style="background:#4a4a5a"></span>
  </div>
  <div class="kin-foot">Kinloop social plugin</div>
</div>

<footer class="abs site-footer">
  Etiam massa dui, condimentum eget lectus id, dapibus pretium arcu.<br>
  Ut auctor erat ac pellentesque molestie.<br>
  Copyright 2014
</footer>

</body>
</html>
```